High End Business Card Design for Flooring Store

Looking for a new card design for our hardwood flooring company. We have no print budget for these and are open to cards made from wood, metal, cardstock with embossed print ... or any combination of these. No plastic.

We sell luxury products and I want the cards to reflect our image of quality and class.

Our contact information as such;
Employee Name
418 Colbrook Blvd.
Harwick, ON
K9R-3M5
(555) 214-3968
Employee email @velkaflooring.com

Target Market(s)

Home Builders

Contact Information for Business Card

Emnployee name, business contact information

```html
<!DOCTYPE html>
<html lang="en">
<head>
<meta charset="utf-8">
<title>Velka Business Card</title>
<link href="https://fonts.googleapis.com/css2?family=Montserrat:wght@400;500&display=swap" rel="stylesheet">
<style>
  :root {
    --backdrop: #808080;
    --card-dark: #1f1f1f;
    --card-light: #ffffff;
    --brand-red: #952c26;
    --brand-gold: #e8b22b;
    --text-grey: #5e5e5e;
    --tagline-grey: #6e6e6e;
    --rule-grey: #e6e6e6;
  }
  html, body {
    margin: 0;
    padding: 0;
    width: 1200px;
    height: 1194px;
    overflow: hidden;
    background: var(--backdrop);
    font-family: "Montserrat", sans-serif;
  }
  .card {
    position: absolute;
    left: 278px;
    width: 644px;
    height: 376px;
    overflow: hidden;
  }
  .card--front { top: 181px; background: var(--card-dark); }
  .card--back  { top: 683px; background: var(--card-light); }

  .brand { position: absolute; text-align: center; }
  .brand__row { display: flex; align-items: center; gap: 8px; }
  .brand__square { background: var(--brand-gold); flex: none; }
  .brand__name {
    color: var(--brand-red);
    font-weight: 500;
    line-height: 1;
    letter-spacing: 0.01em;
  }
  .brand__tagline { color: var(--tagline-grey); font-weight: 400; line-height: 1.05; }

  .card--front .brand { left: 62px; top: 146px; width: 330px; }
  .card--front .brand__square { width: 38px; height: 38px; }
  .card--front .brand__name { font-size: 82px; }
  .card--front .brand__tagline { font-size: 20px; margin-top: -6px; padding-left: 44px; }

  .card--back .brand { left: 42px; top: 36px; width: 200px; }
  .card--back .brand__square { width: 22px; height: 22px; }
  .card--back .brand__row { gap: 6px; }
  .card--back .brand__name { font-size: 44px; }
  .card--back .brand__tagline { font-size: 12.5px; margin-top: -4px; padding-left: 28px; }

  .person { position: absolute; left: 44px; top: 146px; }
  .person__name { color: var(--text-grey); font-size: 31px; font-weight: 400; line-height: 1; letter-spacing: 0.02em; }
  .person__title { color: var(--brand-red); font-size: 15px; margin-top: -2px; }

  .rule { position: absolute; left: 36px; top: 224px; width: 572px; height: 4px; background: var(--rule-grey); }

  .contact { position: absolute; left: 44px; top: 262px; margin: 0; padding: 0; list-style: none; }
  .contact__item { display: flex; align-items: center; gap: 16px; height: 27px; color: var(--text-grey); font-size: 15px; letter-spacing: 0.02em; }
  .contact__icon { width: 16px; height: 16px; flex: none; }

  .address { position: absolute; left: 398px; top: 266px; margin: 0; font-style: normal; color: var(--text-grey); font-size: 15px; line-height: 20.5px; letter-spacing: 0.02em; }
</style>
</head>
<body>
  <section class="card card--front">
    <div class="brand">
      <div class="brand__row">
        <span class="brand__square"></span>
        <span class="brand__name">Velka</span>
      </div>
      <div class="brand__tagline">Planchers &amp; Escaliers<br>Flooring &amp; Stairs</div>
    </div>
  </section>

  <section class="card card--back">
    <div class="brand">
      <div class="brand__row">
        <span class="brand__square"></span>
        <span class="brand__name">Velka</span>
      </div>
      <div class="brand__tagline">Planchers &amp; Escaliers<br>Flooring &amp; Stairs</div>
    </div>

    <div class="person">
      <div class="person__name">YOUR NAME</div>
      <div class="person__title">Your Title</div>
    </div>

    <div class="rule"></div>

    <ul class="contact">
      <li class="contact__item">
        <svg class="contact__icon" viewBox="0 0 16 16" aria-hidden="true">
          <circle cx="8" cy="8" r="8" fill="var(--brand-gold)"/>
          <path d="M5.2 4.6c.4-.3.8-.2 1 .2l.6 1.2c.2.3.1.6-.2.8l-.4.3c.4.9 1.1 1.6 2 2l.3-.4c.2-.3.5-.4.8-.2l1.2.6c.4.2.5.6.2 1l-.5.6c-.4.4-1 .5-1.6.3-1.900-.8-3.3-2.2-4.1-4.1-.2-.6-.1-1.2.3-1.6z" fill="#fff"/>
        </svg>
        <span>(555) 214-3968</span>
      </li>
      <li class="contact__item">
        <svg class="contact__icon" viewBox="0 0 16 16" aria-hidden="true">
          <circle cx="8" cy="8" r="8" fill="var(--brand-gold)"/>
          <rect x="4.3" y="5.5" width="7.4" height="5" fill="none" stroke="#fff" stroke-width="0.9"/>
          <path d="M4.3 5.5 8 8.4l3.7-2.9" fill="none" stroke="#fff" stroke-width="0.9"/>
        </svg>
        <span>employee@velkaflooring.com</span>
      </li>
    </ul>

    <address class="address">418 Colbrook Blvd.<br>Harwick, ON<br>K9R-3M5</address>
  </section>
</body>
</html>
```